Business Card Design For Marketing Agnecy LVT

Need business card design for marketing agency.

Dorian Pell
President, CEO
1-555-304-2917
dorian@lumenvaletrewards.net
www.LumenValeTrewards.biz

Back Side:
Boost Sales Using Rewards, Incentives & Giveaways
Get A Free Sample Package

Target Market(s)

B2B

Industry/Entity Type

Marketing

Contact Information for Business Card

Dorian Pell
President, CEO
1-555-304-2917

Back Side:
Get A Free Sample Package

Please note that my current url is OLD DESIGN. I am working on new design and want the business card to match color themes at least on new site. Here is the demo link for new site so you can see the colors I use, etc.

http://pagekilnstudio.example/qx/dorian/lvt_final/index.html

Requirements
Must have
• Please note that my current url is OLD DESIGN. I am working on new design and want the business card to match color themes at least on new site. Here is the demo link for new site so you can see the colors I use, etc.

Nice to have

Should not have

```html
<!DOCTYPE html>
<html lang="en">
<head>
<meta charset="utf-8">
<title>LVT Business Card</title>
<link href="https://fonts.googleapis.com/css2?family=Lato:ital,wght@0,400;0,700;1,400&family=Montserrat:wght@600&display=swap" rel="stylesheet">
<style>
  :root {
    --stage: #333436;
    --brand-blue: #4d7dbf;
    --brand-blue-light: #6495cf;
    --brand-blue-deep: #4a76b5;
    --ink-gray: #5e5f62;
    --card-white: #ffffff;
    --card-mist: #e9e9ea;
    --text-dark: #4a4b4d;
  }
  * { margin: 0; padding: 0; box-sizing: border-box; }
  html, body { width: 1200px; height: 985px; overflow: hidden; }
  body {
    background: var(--stage);
    font-family: 'Lato', sans-serif;
    position: relative;
  }
  .card {
    position: absolute;
    left: 307px;
    width: 586px;
    height: 334px;
    border-radius: 23px;
    overflow: hidden;
  }
  .card--front {
    top: 141px;
    background: radial-gradient(ellipse at 45% 75%, var(--card-white) 0%, var(--card-white) 35%, var(--card-mist) 100%);
  }
  .card--back {
    top: 509px;
    background: radial-gradient(ellipse at 30% 10%, var(--brand-blue-light) 0%, var(--brand-blue) 55%, var(--brand-blue-deep) 100%);
    color: var(--card-white);
    text-align: center;
  }
  .front-waves { position: absolute; inset: 0; width: 586px; height: 334px; }

  .brand-name {
    position: absolute;
    font-family: 'Lato', sans-serif;
    font-weight: 700;
    line-height: 1;
  }
  .card--front .brand-name { left: 35px; top: 58px; color: var(--brand-blue); font-size: 88px; }
  .card--back .brand-name { left: 0; width: 100%; top: 80px; color: var(--card-white); font-size: 110px; }

  .person {
    position: absolute;
    right: 40px;
    top: 56px;
    text-align: right;
  }
  .person__name {
    font-family: 'Montserrat', sans-serif;
    font-weight: 600;
    font-size: 25px;
    color: var(--brand-blue);
    letter-spacing: 0.3px;
    line-height: 1;
  }
  .person__title { font-size: 14px; color: var(--text-dark); margin-top: 2px; }

  .contact-list { position: absolute; left: 33px; top: 199px; list-style: none; }
  .contact-list li {
    display: flex; align-items: center; gap: 6px;
    height: 21.5px;
    font-size: 13.5px; color: var(--text-dark);
  }
  .contact-list svg { width: 18px; height: 18px; flex: none; }

  .address {
    position: absolute; right: 40px; top: 273px;
    text-align: right; font-size: 13px; line-height: 19.5px; color: var(--card-white);
    font-style: normal;
  }

  .tagline { position: absolute; top: 243px; width: 100%; font-size: 13.5px; }
  .offer { position: absolute; top: 268px; width: 100%; font-size: 13.5px; font-weight: 700; }
  .site { position: absolute; top: 287px; width: 100%; font-size: 15px; font-style: italic; }
  .site__domain { color: var(--ink-gray); }
</style>
</head>
<body>

<section class="card card--front">
  <svg class="front-waves" viewBox="0 0 586 334" aria-hidden="true">
    <path d="M0,306 C210,302 420,262 586,201 L586,334 L0,334 Z" fill="var(--brand-blue)"/>
    <path d="M0,287 C190,290 350,276 459,246 C360,280 200,298 0,302 Z" fill="var(--ink-gray)"/>
  </svg>

  <div class="brand-name">LVT</div>

  <div class="person">
    <div class="person__name">DORIAN PELL</div>
    <div class="person__title">President, CEO</div>
  </div>

  <ul class="contact-list">
    <li>
      <svg viewBox="0 0 18 18"><circle cx="9" cy="9" r="8" fill="none" stroke="var(--ink-gray)" stroke-width="1.2"/><path d="M6 5.2l1.6-.4.9 2-1 .8a5 5 0 0 0 2.4 2.4l.8-1 2 .9-.4 1.6c-3.5.3-6.6-2.8-6.3-6.3z" fill="var(--brand-blue)"/></svg>
      <span>1-555-304-2917</span>
    </li>
    <li>
      <svg viewBox="0 0 18 18"><circle cx="9" cy="9" r="8" fill="none" stroke="var(--ink-gray)" stroke-width="1.2"/><rect x="5" y="6" width="8" height="6" rx="1" fill="var(--brand-blue)"/><path d="M5.3 6.5L9 9.3l3.7-2.8" fill="none" stroke="#fff" stroke-width="0.9"/></svg>
      <span>dorian@lumenvaletrewards.net</span>
    </li>
    <li>
      <svg viewBox="0 0 18 18"><circle cx="9" cy="9" r="8" fill="none" stroke="var(--ink-gray)" stroke-width="1.2"/><g fill="none" stroke="var(--brand-blue)" stroke-width="0.9"><circle cx="9" cy="9" r="4.5"/><ellipse cx="9" cy="9" rx="2" ry="4.5"/><path d="M4.5 9h9M5.2 6.8h7.6M5.2 11.2h7.6"/></g></svg>
      <span>www.LumenValeTrewards.biz</span>
    </li>
  </ul>

  <address class="address">
    4470 Harbor Crest Way<br>Brightwater, CA 90417, USA
  </address>
</section>

<section class="card card--back">
  <div class="brand-name">LVT</div>
  <p class="tagline">Boost Sales Using Rewards, Incentives &amp; Giveaways</p>
  <p class="offer">Get A Free Sample Package</p>
  <p class="site">www.<span class="site__domain">LumenValeTrewards</span>.biz</p>
</section>

</body>
</html>
```